Lumo Ket

Need business cards designed. Project is an Arts Center in Hollywood. It'll include 3 live theatre, a restaurant and event space.

Target Market(s)

Across the board, young and old.

Industry/Entity Type

Entertainment

Contact Information for Business Card

Be creative. This is a creative venture that I'm building.

```html
<!DOCTYPE html>
<html lang="en">
<head>
<meta charset="utf-8">
<title>Lumo Ket – Business Card</title>
<link href="https://fonts.googleapis.com/css2?family=Bodoni+Moda:wght@400&family=Jost:wght@400&display=swap" rel="stylesheet">
<style>
  :root {
    --paper: #ffffff;
    --ink: #111111;
    --night: #000000;
    --silver: #c9c9c9;
    --muted: #9a9a9a;
    --backdrop: #ebebea;
  }
  html, body { margin: 0; padding: 0; overflow: hidden; }
  body { width: 1194px; height: 1200px; background: var(--backdrop); position: relative; }

  .card { position: absolute; top: 0; height: 348px; width: 597px; overflow: hidden; }
  .card--front { left: 0; background: var(--paper); }
  .card--back { left: 597px; background: var(--night); }

  .brand-name {
    position: absolute; left: 176px; top: 110px; margin: 0;
    font-family: "Jost", sans-serif; font-weight: 400; font-size: 66px;
    color: var(--ink); letter-spacing: 1px; line-height: 1;
  }
  .tagline {
    position: absolute; left: 333px; top: 205px; margin: 0;
    font-family: "Jost", sans-serif; font-size: 14.5px; line-height: 17px;
    color: var(--ink); text-transform: uppercase; letter-spacing: 0.3px;
  }

  .venue-photo {
    position: absolute; left: 250px; top: 40px; width: 347px; height: 230px;
    background: radial-gradient(ellipse at 45% 50%, #3a3a3a 0%, #1c1c1c 45%, #000 80%);
  }
  .holder-name {
    position: absolute; left: 42px; top: 108px; margin: 0;
    font-family: "Bodoni Moda", serif; font-weight: 400; color: var(--muted);
    font-size: 24px; letter-spacing: 2px; text-transform: uppercase; white-space: nowrap;
  }
  .holder-name .initial { font-size: 92px; color: #e6e6e6; letter-spacing: 0; vertical-align: -8px; }

  .contact { position: absolute; top: 262px; font-family: "Jost", sans-serif; font-size: 15px;
    line-height: 20px; color: var(--silver); letter-spacing: 0.4px; text-transform: uppercase; }
  .contact svg { display: block; margin-bottom: 2px; }
  .contact--address { left: 42px; }
  .contact--phone { left: 271px; }
  .contact--email { left: 413px; text-transform: none; }
</style>
</head>
<body>
  <section class="card card--front">
    <p class="brand-name">Lumo Ket</p>
    <p class="tagline">Live theatre,<br>a restaurant and<br>event space.</p>
  </section>

  <section class="card card--back">
    <div class="venue-photo" role="img" aria-label="Night photograph of the arts center building with large illuminated show posters"></div>
    <p class="holder-name">Marin <span class="initial">V</span>osk</p>

    <div class="contact contact--address">
      <svg width="14" height="14" viewBox="0 0 14 14"><circle cx="7" cy="7" r="7" fill="#fff"/><path d="M7 3a2.5 2.5 0 0 0-2.5 2.5C4.5 7.5 7 10.5 7 10.5S9.5 7.5 9.5 5.5A2.5 2.5 0 0 0 7 3z" fill="#000"/><circle cx="7" cy="5.5" r="0.9" fill="#fff"/></svg>
      412 N. Verano Ave.<br>Los Angeles, CA 90038
    </div>
    <div class="contact contact--phone">
      <svg width="14" height="14" viewBox="0 0 14 14"><circle cx="7" cy="7" r="7" fill="#fff"/><path d="M4.5 4c.5-.6 1.2-.5 1.5.1l.5 1c.2.4 0 .8-.3 1l-.4.3c.4.9 1 1.5 1.9 1.9l.3-.4c.3-.3.7-.5 1-.3l1 .5c.6.3.7 1 .1 1.5-1 .9-2.6.6-4-.8S3.6 5 4.5 4z" fill="#000"/></svg>
      323.555.0148
    </div>
    <div class="contact contact--email">
      <svg width="14" height="14" viewBox="0 0 14 14"><circle cx="7" cy="7" r="7" fill="#fff"/><rect x="3.5" y="4.5" width="7" height="5" rx="0.6" fill="#000"/><path d="M3.8 4.9 7 7.3l3.2-2.4" stroke="#fff" stroke-width="0.8" fill="none"/></svg>
      mvosk@lumoket.com
    </div>
  </section>
</body>
</html>
```